Pennick - Eggs For Sale Sign

Would like a graphic quality image of a EGGS FOR SALE SIGN ... am getting a local outdoor sign company to print the sign and attach it to a frame.

this is going to be outside by the gate to our farm ... would like the sign to "POP" ... DRAW ATTENTION ... as it were ... please.

I think we need it about 36”(w) x 30”(h) ... maybe 48”x36” ... not sure ... need about an extra 1 1/2” border around also so that we can frame this into a wooden frame ...

The color picture is similar to the pattern we like ... the fonts you are welcome to just blow us out of the water with ... we are not tied down to any particular font ... like the “WANTED” posters of old ... sorta.

Logo Text

Quill Bend Acres

Colors

Designer to choose colors to be used in the design.

Requirements
Must have
• Some type of Fire Fly art ... not to modern ... not too comic book ...
Nice to have
• phone number
• call or text

```html
<!DOCTYPE html>
<html lang="en">
<head>
<meta charset="utf-8">
<title>Quill Bend Acres – Eggs For Sale</title>
<link rel="stylesheet" href="https://fonts.googleapis.com/css2?family=Abril+Fatface&family=Alfa+Slab+One&family=Rye&family=Saira+Condensed:wght@500&display=swap">
<style>
  :root {
    --wood-light: #c9a888;
    --wood-mid: #b8977a;
    --wood-dark: #a8866a;
    --ink: #111111;
    --ink-soft: #2e2e2e;
    --paper: #e8eff1;
    --halo: rgba(160, 195, 208, 0.6);
    --slate: #5f8c9b;
    --ray: #a9c6d1;
    --silhouette: #2b2b2b;
    --ornament: #3a3431;
    --white: #ffffff;
  }
  html, body {
    margin: 0;
    padding: 0;
    width: 1200px;
    height: 900px;
    overflow: hidden;
    background: #ffffff;
  }
  .sign {
    display: block;
    width: 1200px;
    height: 900px;
  }
  .brand-name {
    font-family: "Rye", serif;
    font-size: 150px;
    fill: var(--ink);
  }
  .tagline {
    font-family: "Saira Condensed", sans-serif;
    font-weight: 500;
    font-size: 62px;
    fill: var(--ink-soft);
    stroke: var(--white);
    stroke-width: 5px;
    paint-order: stroke;
  }
  .arc-line {
    font-family: "Saira Condensed", sans-serif;
    font-weight: 500;
    font-size: 66px;
    fill: var(--ink-soft);
  }
  .headline {
    font-family: "Abril Fatface", serif;
    font-size: 240px;
    fill: var(--ink);
  }
  .band-text {
    font-family: "Alfa Slab One", serif;
    font-size: 82px;
    fill: var(--ink);
  }
  .phone {
    font-family: "Alfa Slab One", serif;
    font-size: 80px;
    fill: var(--ink);
    stroke: var(--white);
    stroke-width: 8px;
    paint-order: stroke;
  }
  .frame-line {
    fill: none;
    stroke: var(--ink-soft);
    stroke-width: 3;
  }
</style>
</head>
<body>
<svg class="sign" viewBox="0 0 1200 900" xmlns="http://www.w3.org/2000/svg">
  <defs>
    <linearGradient id="woodTone" x1="0" y1="0" x2="1" y2="1">
      <stop offset="0" stop-color="#c9a888"/>
      <stop offset="0.5" stop-color="#b8977a"/>
      <stop offset="1" stop-color="#a8866a"/>
    </linearGradient>
    <path id="arcPath" d="M 262 534 A 346 204 0 0 1 954 534"/>
  </defs>

  <rect class="board" role="img" aria-label="Weathered wooden plank background" x="0" y="0" width="1200" height="900" fill="url(#woodTone)"/>

  <g class="frame">
    <line class="frame-line" x1="120" y1="32" x2="1080" y2="32"/>
    <line class="frame-line" x1="120" y1="52" x2="1080" y2="52"/>
    <line class="frame-line" x1="120" y1="852" x2="1080" y2="852"/>
    <line class="frame-line" x1="120" y1="870" x2="1080" y2="870"/>
    <line class="frame-line" x1="32" y1="120" x2="32" y2="780"/>
    <line class="frame-line" x1="50" y1="120" x2="50" y2="780"/>
    <line class="frame-line" x1="1168" y1="120" x2="1168" y2="780"/>
    <line class="frame-line" x1="1150" y1="120" x2="1150" y2="780"/>
  </g>

  <g class="corners" fill="var(--ornament)" opacity="0.55">
    <rect role="img" aria-label="Scroll corner ornament" x="16" y="16" width="104" height="88" rx="6"/>
    <rect role="img" aria-label="Scroll corner ornament" x="1080" y="16" width="104" height="88" rx="6"/>
    <rect role="img" aria-label="Scroll corner ornament" x="16" y="776" width="104" height="108" rx="6"/>
    <rect role="img" aria-label="Scroll corner ornament" x="1080" y="776" width="104" height="108" rx="6"/>
  </g>

  <g class="brand">
    <text class="brand-name" x="96" y="204" textLength="464" lengthAdjust="spacingAndGlyphs">QUILL BEND</text>
    <circle class="firefly-mark" role="img" aria-label="Firefly emblem" cx="652" cy="150" r="58" fill="var(--ink)"/>
    <text class="brand-name" x="744" y="204" textLength="368" lengthAdjust="spacingAndGlyphs">ACRES</text>
  </g>

  <text class="tagline" x="76" y="288" textLength="196" lengthAdjust="spacingAndGlyphs">ORIGINAL</text>
  <text class="tagline" x="1128" y="288" text-anchor="end" textLength="244" lengthAdjust="spacingAndGlyphs">FREE RANGE</text>

  <g class="egg-badge">
    <ellipse cx="608" cy="452" rx="420" ry="228" fill="var(--halo)"/>
    <ellipse role="img" aria-label="Pale blue sunburst rays inside the egg" cx="608" cy="514" rx="282" ry="160" fill="var(--paper)" stroke="var(--slate)" stroke-width="6"/>
    <ellipse cx="608" cy="514" rx="200" ry="112" fill="var(--ray)" opacity="0.35"/>
    <text class="arc-line"><textPath href="#arcPath" startOffset="50%" text-anchor="middle" textLength="800" lengthAdjust="spacing">FRESH FROM THE FARM</textPath></text>
    <text class="headline" x="614" y="600" text-anchor="middle" textLength="436" lengthAdjust="spacingAndGlyphs">EGGS</text>
  </g>

  <rect class="hen" role="img" aria-label="Black hen silhouette facing right" x="212" y="524" width="116" height="136" rx="40" fill="var(--silhouette)"/>
  <rect class="hen" role="img" aria-label="Black hen silhouette facing left" x="892" y="524" width="116" height="136" rx="40" fill="var(--silhouette)"/>

  <g class="sale-band">
    <rect x="154" y="664" width="892" height="110" rx="55" fill="var(--paper)" stroke="var(--slate)" stroke-width="8"/>
    <text class="band-text" x="602" y="748" text-anchor="middle" textLength="756" lengthAdjust="spacingAndGlyphs">FOR SALE</text>
  </g>

  <text class="phone" x="600" y="842" text-anchor="middle" textLength="680" lengthAdjust="spacingAndGlyphs">(555) 014-2386</text>
</svg>
</body>
</html>
```